Business Card Design for Cybersecurity Company - Quorvent Systems

We need a business card design for our new cybersecurity company, Quorvent. We’re going for a clean, hi tech look that feels modern, premium, and trustworthy. We want a design that really stands out and makes people say WOW when we hand it over!

Quorvent delivers reliable IT support and managed services for small and mid sized businesses. We help companies stay secure, efficient, and connected through proactive monitoring, cybersecurity services, cloud management, and remote support.

Target Market(s)

Designers should target small and mid sized businesses that need dependable cybersecurity and IT support.

Industry/Entity Type

Cybersecurity, Managed Service Provider, IT services

Contact Information for Business Card

Contact information

Requirements
Must have
• The card should look clean, modern, and tech focused, with the Quorvent logo, clear contact info, and strong readability. It needs to feel premium and professional while still keeping a simple layout that fits a cybersecurity and IT brand.
Nice to have
• Nice to have elements include subtle touches that give the card a modern, tech feel, along with a layout that works well in different background styles.
Should not have
• The card should avoid clutter, loud graphics, or anything that takes attention away from the logo and contact details.

```html
<!DOCTYPE html>
<html lang="en">
<head>
<meta charset="utf-8">
<title>Quorvent Systems – Business Card</title>
<link rel="stylesheet" href="https://fonts.googleapis.com/css2?family=Arimo:wght@400;700&display=swap">
<style>
  :root {
    --stage: #b4b4b4;
    --card-white: #ffffff;
    --grad-teal: #0a82cc;
    --grad-blue: #3c57ee;
    --grad-violet: #6b2ee2;
    --brand-blue: #0f78c8;
    --brand-mark: #4a3fe0;
    --ink: #111318;
    --trace: #e6eef7;
    --shadow: rgba(0, 0, 0, 0.28);
  }
  * { box-sizing: border-box; margin: 0; padding: 0; }
  html, body { width: 1200px; height: 1044px; overflow: hidden; }
  body {
    background: var(--stage);
    font-family: "Arimo", Arial, sans-serif;
    position: relative;
  }
  .card {
    position: absolute;
    width: 630px;
    height: 360px;
    border-radius: 22px;
    overflow: hidden;
    box-shadow: 0 10px 24px var(--shadow);
  }
  .card--front {
    left: 120px;
    top: 120px;
    background: linear-gradient(30deg, var(--grad-teal) 0%, var(--grad-blue) 55%, var(--grad-violet) 100%);
  }
  .card--back {
    left: 450px;
    top: 560px;
    background: var(--card-white);
  }
  .trace-field {
    position: absolute;
    inset: 0;
    background: radial-gradient(ellipse at 50% 50%, rgba(255,255,255,0.08), rgba(255,255,255,0) 70%);
  }
  .brand {
    position: absolute;
    display: flex;
    align-items: center;
    gap: 12px;
    font-weight: 700;
    font-size: 34px;
    letter-spacing: 0.5px;
    white-space: nowrap;
  }
  .brand__dot {
    width: 26px;
    height: 26px;
    border-radius: 50%;
  }
  .card--front .brand {
    left: 50%;
    top: 50%;
    transform: translate(-50%, -50%);
    color: #ffffff;
  }
  .card--front .brand__dot { background: #ffffff; }
  .card--back .brand {
    right: 40px;
    top: 52px;
    font-size: 28px;
    color: var(--brand-mark);
  }
  .card--back .brand__dot { background: var(--brand-mark); width: 22px; height: 22px; }
  .back-traces {
    position: absolute;
    right: 0;
    bottom: 0;
    width: 420px;
    height: 210px;
    background: linear-gradient(160deg, rgba(230,238,247,0) 0%, var(--trace) 100%);
    opacity: 0.7;
  }
  .website {
    position: absolute;
    right: 40px;
    top: 176px;
    display: flex;
    align-items: center;
    gap: 8px;
    font-size: 16px;
    color: var(--ink);
  }
  .website__icon {
    width: 14px; height: 14px; border-radius: 50%;
    background: var(--brand-blue);
  }
  .person {
    position: absolute;
    left: 46px;
    top: 150px;
  }
  .person__name {
    font-size: 36px;
    font-weight: 400;
    color: var(--brand-blue);
    line-height: 1;
  }
  .person__role {
    margin-top: 6px;
    font-size: 11px;
    color: var(--ink);
  }
  .contacts {
    position: absolute;
    left: 46px;
    top: 232px;
    list-style: none;
  }
  .contacts li {
    display: flex;
    align-items: center;
    gap: 10px;
    font-size: 17px;
    color: var(--ink);
    height: 30px;
  }
  .contacts svg { width: 16px; height: 16px; flex: none; }
</style>
</head>
<body>

<section class="card card--front" aria-label="Card front">
  <div class="trace-field" role="img" aria-label="Faint circuit trace pattern across the card"></div>
  <div class="brand"><span class="brand__dot"></span>Quorvent Systems</div>
</section>

<section class="card card--back" aria-label="Card back">
  <div class="back-traces" role="img" aria-label="Pale circuit trace pattern in the lower right"></div>
  <div class="brand"><span class="brand__dot"></span>Quorvent Systems</div>

  <div class="website"><span class="website__icon"></span>quorvent.com</div>

  <div class="person">
    <h1 class="person__name">Dalen Marsh</h1>
    <p class="person__role">Owner | CEO | Quorvent Systems</p>
  </div>

  <ul class="contacts">
    <li>
      <svg viewBox="0 0 16 16" aria-hidden="true"><path d="M3 1.5l2.6 0 1 3.2-1.6 1.2a9 9 0 0 0 5.1 5.1l1.2-1.6 3.2 1v2.6c0 .8-.7 1.5-1.5 1.5C6.8 14.5 1.5 9.2 1.5 3c0-.8.7-1.5 1.5-1.5z" fill="#0f78c8"/></svg>
      P: (855) 310-4782
    </li>
    <li>
      <svg viewBox="0 0 16 16" aria-hidden="true"><rect x="3.5" y="1" width="9" height="14" rx="1.5" fill="none" stroke="#0f78c8" stroke-width="1.5"/></svg>
      M: (813) 555-0193
    </li>
    <li>
      <svg viewBox="0 0 16 16" aria-hidden="true"><rect x="1" y="3" width="14" height="10" fill="#0f78c8"/><path d="M1 3l7 6 7-6" fill="none" stroke="#ffffff" stroke-width="1.2"/></svg>
      E: dalen@quorvent.com
    </li>
  </ul>
</section>

</body>
</html>
```